Moroccan Wordpress Keluma Exhibit Design

We seek a new website for Keluma (VarenStoneQuest.org), an exhibit of The Tolvek Initiative’s Atlas Hall of Coastal Heritage Ways, dedicated to uncovering the “buried” or “covered” Jewish treasures of Morocco.
Spanning the entire country, from metropolitan centers to remote villages, Keluma proffers a virtual passport to visitors wishing to explore mountain-top shrines of Jewish “saints” that continue to be voluntarily protected by Muslim caretakers, scorpion-guarded genizot (burial grounds for holy texts and objects), anthropomorphic tombstones in seaside cemeteries, synagogues on the edge of the Sahara Desert, and ancient urban quarters with hidden reminders of their one-time residents.
This exhibit marks the first public showing of documentation on the majority of these sites, including several Vichy regime desert labor and “discipline” camps where hundreds of Jews and non-Jewish political prisoners toiled, suffered torture, and died during the Holocaust.
Keluma is certainly the first to feature:
* Extensive documentation on Jewish sites in major cities and remote settings alike;
* Exclusive immersive panoramas, three-dimensional reconstructions, high-definition videos, site summaries, cultural atlas, archival and contemporary photos; and
* Interactive virtual tours of sites led by Morocco’s only Jewish guide.
Keluma's website design needs to be clean and informational and exciting as well as showcase the best of our collection. The winning design should include an intuitive interface and taxonomy capable of handling hundreds of site entries.
The template should also have a distinctive homepage, themed pages (curator's introduction, staff, screening rooms to view multimedia content, virtual tours, behind-the-scenes, contribute), and no blog elements (e.g., comment section). Admin friendliness is a plus.

```html
<!DOCTYPE html>
<html lang="en">
<head>
<meta charset="utf-8">
<title>Keluma : Jewish Treasures of Southern Morocco</title>
<link href="https://fonts.googleapis.com/css2?family=Ubuntu:wght@400;500&family=Dancing+Script:wght@500&display=swap" rel="stylesheet">
<style>
  :root {
    --sky-top: #f4f4f1;
    --sky-bottom: #ebebe6;
    --sand-top: #f7ecd8;
    --sand-bottom: #e1b47c;
    --title: #b5622a;
    --accent: #d86a1c;
    --body-text: #a05c18;
    --rule: #f0d070;
    --frame: #e07a2c;
    --scene-dark: rgba(107, 68, 48, 0.85);
    --scene-mid: rgba(160, 110, 72, 0.55);
    --scene-fade: rgba(235, 235, 230, 0);
    --photo-wall: #9e8a70;
    --photo-blue: #2e5fbf;
  }
  * { margin: 0; padding: 0; box-sizing: border-box; }
  html, body { width: 1200px; height: 900px; overflow: hidden; }
  body { font-family: "Ubuntu", "Trebuchet MS", sans-serif; position: relative; }

  .masthead {
    position: absolute; left: 0; top: 0; width: 1200px; height: 438px;
    background: linear-gradient(180deg, var(--sky-top), var(--sky-bottom));
    border-bottom: 1px solid var(--rule);
  }
  .site-title {
    position: absolute; left: 73px; top: 86px;
    font-weight: 400; font-size: 30px; color: var(--title); letter-spacing: 0.2px;
  }
  .site-subtitle {
    position: absolute; right: 480px; top: 128px;
    font-weight: 400; font-size: 18px; color: var(--accent);
  }
  .header-scene {
    position: absolute; left: 565px; top: 145px; width: 635px; height: 293px;
    background: radial-gradient(ellipse 70% 80% at 45% 85%, var(--scene-dark) 0%, var(--scene-mid) 45%, var(--scene-fade) 100%);
  }
  .main-nav { position: absolute; left: 0; top: 405px; }
  .main-nav a {
    position: absolute; top: 0; white-space: nowrap;
    font-family: "Dancing Script", cursive; font-size: 21px;
    color: var(--accent); text-decoration: none;
  }

  .content {
    position: absolute; left: 0; top: 439px; width: 1200px; height: 461px;
    background: linear-gradient(180deg, var(--sand-top), var(--sand-bottom));
  }
  .feature-frame {
    position: absolute; left: 0; top: 35px; width: 380px; height: 331px;
    border: 1px solid var(--frame); border-left: none;
  }
  .feature-frame .edge {
    position: absolute; top: -1px; height: 331px; width: 1px; background: var(--frame);
  }
  .feature-photo {
    position: absolute; left: 0; top: 3px; width: 352px; height: 326px;
    background: linear-gradient(160deg, #c9b79c 0%, var(--photo-wall) 45%, #6f5c48 75%, var(--photo-blue) 100%);
  }
  .intro {
    position: absolute; left: 416px; top: 35px; width: 745px;
    font-size: 12.6px; line-height: 16px; color: var(--body-text);
  }
  .intro p { margin-bottom: 16px; }
  .copyright {
    position: absolute; left: 416px; top: 436px;
    font-size: 10px; color: var(--body-text);
  }
</style>
</head>
<body>
  <header class="masthead">
    <h1 class="site-title">Keluma : Jewish Treasures of Southern Morocco</h1>
    <p class="site-subtitle">Presented by the Tolvek Initiative the Brenhollow Foundation</p>

    <div class="header-scene" role="img" aria-label="Painterly image of a ruined earthen kasbah on a rocky desert hillside"></div>

    <nav class="main-nav">
      <a href="#" style="left:86px">Keluma</a>
      <a href="#" style="left:203px">Tour</a>
      <a href="#" style="left:298px">Panoramas</a>
      <a href="#" style="left:433px">Contact</a>
    </nav>
  </header>

  <main class="content">
    <div class="feature-frame">
      <span class="edge" style="left:356px"></span>
      <span class="edge" style="left:361px"></span>
      <span class="edge" style="left:366px"></span>
      <span class="edge" style="left:371px"></span>
      <span class="edge" style="left:376px"></span>
      <div class="feature-photo" role="img" aria-label="Photograph of an old synagogue interior with plastered walls, a hanging lantern and a blue wooden balustrade"></div>
    </div>

    <section class="intro">
      <p>Jewish heritage tours of Morocco typically cycle through Casablanca, Tangiers, Fez, and Marrakesh. But the Jewish Moroccan heartland lies south of these metropolitan centers, in the towns and villages of the Atlas mountains and Sahara desert. Here, Jewish life punctuated the landscape, legendary rabbis helped sustain rural communities, and a distinctive Judeo-Amazigh (Berber) culture developed over the course of two millennia.</p>
      <p>Decades after the community’s dissolution, the once-vibrant Jewish heritage these sites embody is ubiquitous yet hidden, seemingly indelible but inevitably fading. Where it still exists, it does so behind unmarked walls, just off treacherous dirt trails, deep within mountains, in the annual pilgrimages (hillulot) that attract hundreds of expatriates — and increasingly only in the memories of aging Muslim former neighbors as well as the superstitions that they have bequeathed to their children and grand children. Keluma means “covered” or “buried” in the Moroccan dialect, a fitting–and, in some cases, literal–description of what remains.</p>
      <p>During the Holocaust, France’s Vichy regime established a series of forced labor and “discipline” camps in the region’s far eastern flank where hundreds of Jews and non-Jewish political prisoners toiled and died in the desert. These sites are similarly forgotten, but are important reminders of North Africa’s Holocaust history that has only in recent years begun to attract scholarly interest.</p>
      <p>This exhibit marks the first time that pictures of the majority of these sites (including several Vichy camps) have been made public. In addition to photographs, we present an array of virtual documentation–concise summaries, video tours, oral history recordings, 360-degree panoramas, and geo-mapping data–to provide an exclusive glimpse into the heartland of Jewish heritage in Morocco.</p>
      <p>Come explore these remarkable sites on a unique tour — made possible with the generous support of the Brenhollow Foundation.</p>
    </section>

    <footer class="copyright">Copyright © 2010 Meridian Site Archive, Inc. All Rights Reserved.</footer>
  </main>
</body>
</html>
```